New web design for a service provider in the medical field

We are looking for a new design for our website. We are a company that repairs and sells medical endoscopes. Our customers include doctors and hospitals. Our current website can be found at https://lumenfix.example/en/lumenfix-english.
We need a new web design (without programming) for the following 3 pages:
-Startpage https://lumenfix.example/en/lumenfix-english/
-Used endoscopes https://lumenfix.example/en/used-endoscopes/
-Purchase https://lumenfix.example/en/purchase/
The design should be modern and stylish.
The blue color of the logo should be reflected on the page, but not too intrusive.
I have uploaded the images from the header. If more images are needed, let me know and I will upload them.

Target Market(s)
Doctors and hospitals

```html
<!DOCTYPE html>
<html lang="en">
<head>
<meta charset="utf-8">
<title>Lumenfix – Home page</title>
<link rel="stylesheet" href="https://fonts.googleapis.com/css2?family=Poppins:wght@300;400;500;600;700&display=swap">
<style>
:root{
  --brand:#1e9ad6;
  --brand-dark:#1479b3;
  --sky:#5bbbe9;
  --sky-soft:#eaf5fc;
  --navy:#243848;
  --deep:#0f2230;
  --ink:#2b2b2b;
  --muted:#6b7480;
  --white:#ffffff;
  --board:#ffffff;
}
*{box-sizing:border-box;margin:0;padding:0}
html,body{width:1200px;height:3237px;overflow:hidden;background:var(--board);font-family:"Poppins",Arial,sans-serif;color:var(--ink)}
.board{position:relative;width:1200px;height:3237px}
.board-brand{position:absolute;left:78px;top:86px}
.board-brand .name{font-size:33px;font-weight:600;color:var(--brand-dark);display:flex;align-items:center;gap:10px}
.board-brand .dot{width:14px;height:14px;border-radius:50%;background:var(--brand)}
.board-brand .tag{font-size:14px;font-weight:500;color:var(--brand);margin-top:2px;padding-left:24px}
.board-title{position:absolute;right:183px;top:90px;font-size:40px;font-weight:700;color:#111}

.page{position:absolute;left:195px;top:197px;width:822px;height:3003px;background:var(--sky-soft);box-shadow:0 10px 40px rgba(0,0,0,.22);overflow:hidden}
.abs{position:absolute}

.topbar{left:0;top:0;width:822px;height:26px;background:#dedede;font-size:8px;color:#555;display:flex;align-items:center;padding:0 45px}
.topbar .links{margin-left:auto;display:flex;gap:10px}
.topbar .lang{margin-left:48px;display:flex;gap:4px}
.topbar .lang span{padding:1px 3px}
.topbar .lang .on{background:var(--navy);color:#fff}

.header{left:0;top:26px;width:822px;height:78px;background:#fff;display:flex;align-items:center;padding:0 58px}
.logo{font-size:14px;font-weight:600;color:var(--brand-dark);display:flex;align-items:center;gap:6px}
.logo .dot{width:8px;height:8px;border-radius:50%;background:var(--brand)}
.contact{margin-left:auto;display:flex;gap:18px;align-items:center;font-size:11px;color:#333}
.contact .item{display:flex;gap:6px;align-items:center}
.contact small{display:block;font-size:7px;color:#888}

.nav{left:0;top:104px;width:822px;height:38px;background:var(--brand);display:flex;align-items:center;justify-content:space-around;padding:0 40px;font-size:8px;color:#fff;text-transform:uppercase}
.nav .active{border-bottom:1px solid #fff;padding-bottom:2px}

.hero{left:0;top:142px;width:822px;height:386px;background:#fff;clip-path:polygon(0 0,100% 0,100% 77%,50% 100%,0 77%);z-index:2}
.hero-photo{position:absolute;right:0;top:0;width:470px;height:386px;background:radial-gradient(ellipse at 60% 40%,#3a3f46 0%,#7b8087 35%,#e6e8ea 75%)}
.hero h1{position:absolute;left:67px;top:68px;font-size:26px;font-weight:400;line-height:39px;color:#222}
.hero h1 strong{color:var(--brand);font-weight:600}
.btn{display:inline-flex;align-items:center;gap:6px;background:var(--brand);color:#fff;font-size:10px;padding:4px 10px;white-space:nowrap}
.hero .btn{position:absolute;left:67px;top:215px}

.future{left:0;top:437px;width:822px;height:366px;z-index:1}
.future-text{position:absolute;left:0;top:0;width:410px;height:366px;background:var(--sky);padding:128px 50px 0 60px;color:#fff}
.future-text h2{font-size:17px;font-weight:400;margin-bottom:14px}
.future-text p{font-size:10px;line-height:16px;margin-bottom:12px}
.future-photo{position:absolute;left:410px;top:0;width:412px;height:366px;background:radial-gradient(ellipse at 50% 45%,#4aa9ea 0%,#1666c4 55%,#0d3f8e 100%)}

.intro{left:0;top:803px;width:822px;height:340px;background:linear-gradient(90deg,#62b9e8,#7cc5ec);clip-path:polygon(0 0,100% 0,100% 88%,50% 100%,0 88%);text-align:center;color:#fff;padding:72px 180px 0}
.intro h3{font-size:13px;font-weight:400;line-height:20px;margin-bottom:36px}
.intro p{font-size:8.5px;line-height:13px;margin-bottom:14px}

.makers{left:167px;top:1178px;display:flex;gap:28px}
.makers span{width:143px;height:48px;display:flex;align-items:center;justify-content:center;font-size:13px;font-weight:600;color:#fff;letter-spacing:1px}
.makers .a{background:var(--navy)}.makers .b{background:var(--brand)}.makers .c{background:var(--deep)}

.card{background:#fff;box-shadow:0 3px 10px rgba(0,0,0,.12);padding:40px 22px 0;height:210px;width:240px}
.card .kicker{display:flex;gap:6px;align-items:center;color:var(--brand);font-size:10px}
.card .sub{font-size:9px;margin:4px 0 12px}
.card p{font-size:7.5px;line-height:12px;color:#444;margin-bottom:10px}

.faulty{left:50px;top:1510px;width:722px;height:193px;background:#fff;box-shadow:0 3px 10px rgba(0,0,0,.12)}
.faulty .photo{position:absolute;left:0;top:0;width:322px;height:193px;background:radial-gradient(ellipse at 40% 50%,#8fd0ff 0%,#2f86e0 45%,#0f4fa8 100%)}
.faulty .text{position:absolute;left:398px;top:58px}
.faulty h4{font-size:10px;font-weight:500;color:var(--brand)}
.faulty small{display:block;font-size:7.5px;color:#555;margin:4px 0 16px}
.faulty .lead{font-size:10px;margin-bottom:8px}

.cause{left:0;top:1767px;width:822px;height:405px}
.cause .photo{position:absolute;left:0;top:0;width:358px;height:405px;background:linear-gradient(135deg,#f1f2f3 0%,#c9cdd1 45%,#4a4f55 70%,#d8dcdf 100%)}
.cause .panel{position:absolute;left:358px;top:0;width:464px;height:405px;background:var(--brand);color:#fff;padding:55px 0 0 42px}
.cause h2{font-size:17px;font-weight:400;margin-bottom:24px}
.cause .grid{display:grid;grid-template-columns:197px 197px;row-gap:26px}
.cause .it h5{display:flex;gap:6px;align-items:flex-start;font-size:7.5px;font-weight:500;text-transform:uppercase;line-height:12px}
.cause .it p{font-size:7px;line-height:11px;padding-left:20px;margin-top:8px;opacity:.9;width:160px}

.decision{left:0;top:2268px;width:822px;text-align:center}
.decision h2{font-size:16px;font-weight:500;color:#222}
.feat{position:absolute;width:300px}
.feat h6{display:flex;gap:10px;align-items:center;color:var(--brand);font-size:10px;font-weight:400;margin-bottom:14px}
.feat p{font-size:8px;line-height:13px;color:#333;padding-left:30px}
.decision-btn{left:0;width:822px;top:2651px;text-align:center}

.help-bg{left:0;top:2680px;width:822px;height:200px;background:linear-gradient(180deg,var(--sky-soft),#9ed4f2)}
.help{left:80px;top:2755px;width:680px;height:100px;background:var(--brand);border-radius:8px;z-index:3}
.help .person{position:absolute;left:142px;top:-50px;width:110px;height:150px;border-radius:55px 55px 0 0;background:linear-gradient(180deg,#d9c3b3,#f3f3f3)}
.help .text{position:absolute;left:335px;top:34px;color:#fff}
.help .text h5{font-size:10px;font-weight:400;margin-bottom:10px}
.help .btn{background:#fff;color:var(--brand);font-size:9.5px}

.footer{left:0;top:2845px;width:822px;height:158px;background:var(--navy);color:#fff;z-index:2}
.footer .links{position:absolute;left:87px;top:63px;display:flex;gap:22px;font-size:8px}
.footer .copy{position:absolute;left:87px;top:106px;font-size:6.5px;opacity:.85}
.footer .social{position:absolute;left:640px;top:60px;display:flex;gap:5px}
.footer .social span{width:12px;height:12px;background:#fff;border-radius:2px}
.footer .badges{position:absolute;left:700px;top:50px;display:flex;gap:4px}
.footer .badges span{width:28px;height:28px;border-radius:50%;background:#3b7bd0}
.footer .badges span+span{background:#e79a1f}
</style>
</head>
<body>
<div class="board">
  <div class="board-brand">
    <div class="name"><span class="dot"></span>Lumenfix</div>
    <div class="tag">Precision for every procedure</div>
  </div>
  <div class="board-title">Home page</div>

  <div class="page">
    <div class="abs topbar">
      <span>Cause the outcome matters</span>
      <div class="links"><span>Pickup Order</span><span>About Us</span><span>Contact Us</span></div>
      <div class="lang"><span>DE</span><span class="on">EN</span></div>
    </div>

    <div class="abs header">
      <div class="logo"><span class="dot"></span>Lumenfix</div>
      <div class="contact">
        <div class="item">
          <svg width="18" height="13" viewBox="0 0 18 13"><rect x="1" y="1" width="16" height="11" fill="none" stroke="#1e9ad6" stroke-width="1.3"/><path d="M1 1l8 6 8-6" fill="none" stroke="#1e9ad6" stroke-width="1.3"/></svg>
          info@lumenfix.example
        </div>
        <div class="item">
          <svg width="16" height="16" viewBox="0 0 24 24"><path d="M6 2l4 5-2 3c1 3 3 5 6 6l3-2 5 4-3 4C10 21 3 14 2 5z" fill="none" stroke="#1e9ad6" stroke-width="1.6"/></svg>
          <div>+49 4100 555 010-0<small>Monday – Friday 08:00 – 20:00</small></div>
        </div>
      </div>
    </div>

    <nav class="abs nav">
      <span class="active">Home</span><span>Endoscope repair</span><span>Used endoscope +</span><span>Endoscope system</span><span>Endoscope accesories +</span><span>Purchase</span>
    </nav>

    <section class="abs hero">
      <div class="hero-photo" role="img" aria-label="Close-up photo of a hand holding the control head of a flexible endoscope"></div>
      <h1>PUT YOUR<br>ENDOSCOPE IN<br><strong>RELIABLE HANDS!</strong></h1>
      <span class="btn">Get in touch →</span>
    </section>

    <section class="abs future">
      <div class="future-text">
        <h2>YOUR FUTURE - OUR SERVICE</h2>
        <p>Die Lumenfix GmbH ist auf die Reparatur und den Verkauf flexibler medizinischer Endoskope der Marken Arkon, Vestra und Kairo spezialisiert. Als serviceorientiertes Unternehmen sind wir nach DIN ISO 9001:2015 zertifiziert und stehen Ihnen mit unserem Wissen und unseren Fähigkeiten zur Seite!</p>
        <p>Wir erbringen eine hochwertige und gleichbleibende Qualität durch die Überwachung aller Prozesse. Überzeugen Sie sich selbst!</p>
      </div>
      <div class="future-photo" role="img" aria-label="Abstract blue digital network of glowing points and lines"></div>
    </section>

    <section class="abs intro">
      <h3>Endoscope repairs and second hand endoscopes from<br>Lumenfix – cause the outcome matters!</h3>
      <p>Lumenfix is a privileged partner for the start-up facility or optimisation of existing healthcare facilities, doctor's offices and hospitals. The quality and reliability of our products and our offered service are our best advertisement!</p>
      <p>As a result of optimised processes and highly qualified specialists in our company, we can work very quickly and with high quality for your benefit of least possible restrictions in your doctor's office or in your hospital.</p>
    </section>

    <div class="abs makers"><span class="a">ARKON →</span><span class="b">VESTRA →</span><span class="c">KAIRO →</span></div>

    <div class="abs card" style="left:47px;top:1278px">
      <div class="kicker"><svg width="11" height="11" viewBox="0 0 12 12"><circle cx="6" cy="6" r="4.5" fill="none" stroke="#1e9ad6" stroke-width="1.3"/><circle cx="6" cy="6" r="1.5" fill="#1e9ad6"/></svg>Repair</div>
      <div class="sub">Endoscope repair service</div>
      <p>Manufacturer-independent we repair and maintain endoscopes, individual components (e.g. processors or light sources), accessories and peripherals of the manufacturers Arkon, Vestra and Kairo.</p>
      <span class="btn">Repair Request →</span>
    </div>
    <div class="abs card" style="left:291px;top:1278px">
      <div class="kicker"><svg width="12" height="11" viewBox="0 0 12 11"><path d="M1 4h10l-1.5 6h-7z M3 4l3-3 3 3" fill="none" stroke="#1e9ad6" stroke-width="1.2"/></svg>Sale</div>
      <div class="sub">Used Endoscope</div>
      <p>Our regular stock includes refurbished gastroscopes, colonoscopes, bronchoscopes, cystoscopes and duodenoscopes from the well-known manufacturers Arkon, Vestra and Kairo.</p>
      <span class="btn">Purchase Request →</span>
    </div>
    <div class="abs card" style="left:535px;top:1278px">
      <div class="kicker"><svg width="12" height="10" viewBox="0 0 12 10"><rect x="1" y="1" width="10" height="8" fill="none" stroke="#1e9ad6" stroke-width="1.2"/><path d="M1 4h10" stroke="#1e9ad6"/></svg>Purchase</div>
      <div class="sub">Used Endoscope</div>
      <p>We are very interested in buying your old endoscopes – even defective and dismantled! We offer fair conditions! Please contact us for a purchase offer!</p>
      <span class="btn">Sale Devices →</span>
    </div>

    <div class="abs faulty">
      <div class="photo" role="img" aria-label="Blue scientific illustration of a glowing DNA strand"></div>
      <div class="text">
        <h4>FAULTY ENDOSCOPE?</h4>
        <small>We ensure quick and smooth repairs!</small>
        <div class="lead">Simple place a</div>
        <span class="btn">Pickup order →</span>
      </div>
    </div>

    <section class="abs cause">
      <div class="photo" role="img" aria-label="Photo of endoscopes hanging in a white storage cabinet"></div>
      <div class="panel">
        <h2>CAUSE THE OUTCOME MATTERS!</h2>
        <div class="grid">
          <div class="it"><h5><svg width="13" height="13" viewBox="0 0 14 14"><circle cx="7" cy="7" r="6" fill="none" stroke="#fff"/><path d="M4 7l2 2 4-4" fill="none" stroke="#fff"/></svg>One company for everyone</h5><p>We are a service provider for doctors and hospitals!</p></div>
          <div class="it"><h5><svg width="13" height="13" viewBox="0 0 14 14"><circle cx="7" cy="7" r="6" fill="none" stroke="#fff"/><path d="M4 7l2 2 4-4" fill="none" stroke="#fff"/></svg>Guaranteed service</h5><p>You receive a six-month warranty on all repairs!</p></div>
          <div class="it"><h5><svg width="13" height="13" viewBox="0 0 14 14"><circle cx="7" cy="7" r="6" fill="none" stroke="#fff"/><path d="M4 7l2 2 4-4" fill="none" stroke="#fff"/></svg>Experience characterises us</h5><p>Our team has many years of experience in the business field!</p></div>
          <div class="it"><h5><svg width="13" height="13" viewBox="0 0 14 14"><circle cx="7" cy="7" r="6" fill="none" stroke="#fff"/><path d="M4 7l2 2 4-4" fill="none" stroke="#fff"/></svg>Quality not quantity</h5><p>Reliability and durability instead of inferior replacements!</p></div>
          <div class="it"><h5><svg width="13" height="13" viewBox="0 0 14 14"><circle cx="7" cy="7" r="6" fill="none" stroke="#fff"/><path d="M4 7l2 2 4-4" fill="none" stroke="#fff"/></svg>The product is close to our hearts</h5><p>We repair and sell second-hand flexible endoscopes!</p></div>
          <div class="it"><h5><svg width="13" height="13" viewBox="0 0 14 14"><circle cx="7" cy="7" r="6" fill="none" stroke="#fff"/><path d="M4 7l2 2 4-4" fill="none" stroke="#fff"/></svg>Services for everyone</h5><p>Our service includes the manufacturers Arkon, Vestra and Kairo!</p></div>
        </div>
      </div>
    </section>

    <div class="abs decision"><h2>Lumenfix GmbH, your decision for your future</h2></div>
    <div class="feat" style="left:88px;top:2318px"><h6><svg width="20" height="20" viewBox="0 0 20 20"><circle cx="10" cy="10" r="8" fill="none" stroke="#1e9ad6" stroke-width="1.4"/><path d="M10 5v5l3 2" fill="none" stroke="#1e9ad6" stroke-width="1.4"/></svg>Fast Repair</h6><p>Keep potential disruptions in your doctor's office or in your hospital at minimum as a result of optimized processes and highly qualified specialists in our company</p></div>
    <div class="feat" style="left:417px;top:2318px"><h6><svg width="20" height="20" viewBox="0 0 20 20"><rect x="3" y="4" width="14" height="13" fill="none" stroke="#1e9ad6" stroke-width="1.4"/><path d="M3 8h14M7 2v4M13 2v4" stroke="#1e9ad6" stroke-width="1.4"/></svg>Highly cost efficient</h6><p>Benefit from our first class recommendations and implementation by our experienced staff. Our goals is to find the best solutions together with you at the best lowest price point.</p></div>
    <div class="feat" style="left:88px;top:2416px"><h6><svg width="20" height="20" viewBox="0 0 20 20"><path d="M3 10l7-6 7 6v7H3z" fill="none" stroke="#1e9ad6" stroke-width="1.4"/></svg>On-site service</h6><p>We will gladly pay you a visit to to carry out analysis and repairs on site. Due to our many years of experience – it doesn't get any faster (whiglelithin a 250 km range)</p></div>
    <div class="feat" style="left:417px;top:2416px"><h6><svg width="20" height="20" viewBox="0 0 20 20"><path d="M10 2l7 3v5c0 4-3 7-7 8-4-1-7-4-7-8V5z" fill="none" stroke="#1e9ad6" stroke-width="1.4"/></svg>Loan equipment service</h6><p>Use our service of high-quality loan devices during the downtime of your defective endoscope (limited to stock)</p></div>
    <div class="feat" style="left:88px;top:2522px"><h6><svg width="20" height="20" viewBox="0 0 20 20"><rect x="4" y="2" width="12" height="16" fill="none" stroke="#1e9ad6" stroke-width="1.4"/><path d="M7 7h6M7 10h6M7 13h4" stroke="#1e9ad6" stroke-width="1.2"/></svg>Without a maintenance contract</h6><p>No subscription or other maintenance contract, but one-time and sustainable repair work</p></div>
    <div class="feat" style="left:417px;top:2522px"><h6><svg width="20" height="20" viewBox="0 0 20 20"><circle cx="10" cy="8" r="5" fill="none" stroke="#1e9ad6" stroke-width="1.4"/><path d="M7 12l-2 6 5-2 5 2-2-6" fill="none" stroke="#1e9ad6" stroke-width="1.4"/></svg>First class service</h6><p>Our clients always come first!</p></div>

    <div class="abs decision-btn"><span class="btn">Learn more about Lumenfix →</span></div>

    <div class="abs help-bg"></div>
    <div class="abs help">
      <div class="person" role="img" aria-label="Photo of a smiling customer service agent wearing a headset"></div>
      <div class="text"><h5>HOW CAN WE HELP YOU?</h5><span class="btn">Send us a message →</span></div>
    </div>

    <footer class="abs footer">
      <div class="links"><span>Informations</span><span>About Us</span><span>Contact Us</span><span>TOS</span><span>Copyrights</span><span>Privacy Policy</span></div>
      <div class="copy">© 2022 Lumenfix GmbH</div>
      <div class="social"><span></span><span></span></div>
      <div class="badges"><span></span><span></span></div>
    </footer>
  </div>
</div>
</body>
</html>
```